Zielgruppe
Was machen wir: Datenschutz und Informationssicherheit als Dienstleistung.
Zielgruppe: Mittelständische Unternehmenskunden 500 -5000 Mitarbeiter
Aufgabenstellung
Wir benötigen eine neue Powerpoint Vorlage. Die alte Vorlage ist nicht mehr zeitgemäß.
Format: DIN 16:9
Standardschriftart: Calibri
Zielgruppe: Mittleres und gehobenes Management
CI: Unsere Farben können auf unserer Webseite eingesehen werden.

```html
<!DOCTYPE html>
<html lang="de">
<head>
<meta charset="utf-8">
<title>DSGVO Netzwerkworkshop</title>
<link rel="stylesheet" href="https://fonts.googleapis.com/css2?family=Carlito:wght@400;700&display=swap">
<style>
  :root {
    --brand-blue: #3e5089;
    --brand-blue-light: #4b5f9a;
    --brand-blue-dark: #35467c;
    --brand-orange: #ff8400;
    --text-white: #ffffff;
    --mark-grey: #9aa6c4;
  }
  html, body {
    margin: 0;
    padding: 0;
    width: 1200px;
    height: 675px;
    overflow: hidden;
    background: var(--brand-blue);
  }
  .slide {
    position: relative;
    width: 1200px;
    height: 675px;
    overflow: hidden;
    font-family: "Carlito", "Calibri", sans-serif;
  }
  .slide__backdrop {
    position: absolute;
    inset: 0;
    background:
      linear-gradient(172deg, rgba(255,255,255,0) 30%, rgba(120,140,200,0.18) 42%, rgba(255,255,255,0) 52%),
      linear-gradient(135deg, var(--brand-blue-light) 0%, var(--brand-blue) 45%, var(--brand-blue-dark) 100%);
  }
  .slide__edge {
    position: absolute;
    top: 0;
    width: 12.5px;
    height: 675px;
    background: var(--brand-orange);
  }
  .slide__edge--left { left: 0; }
  .slide__edge--right { right: 0; }
  .slide__title {
    position: absolute;
    inset: 0;
  }
  .title__kicker {
    font-weight: 700;
    font-size: 99px;
    fill: var(--brand-orange);
  }
  .title__main {
    font-weight: 400;
    font-size: 94px;
    fill: var(--text-white);
  }
  .title__focus-label {
    font-size: 52px;
    fill: var(--brand-orange);
  }
  .title__focus-dash,
  .title__focus-topic {
    font-size: 52px;
    fill: var(--text-white);
  }
  .brand-name {
    position: absolute;
    right: 34px;
    bottom: 24px;
    font-size: 15px;
    font-weight: 700;
    color: var(--mark-grey);
    letter-spacing: 0.5px;
  }
</style>
</head>
<body>
  <main class="slide">
    <div class="slide__backdrop" role="img" aria-label="Unscharfes Foto mit blauen Lichtstreifen im Hintergrund"></div>
    <div class="slide__edge slide__edge--left"></div>
    <div class="slide__edge slide__edge--right"></div>

    <svg class="slide__title" width="1200" height="675" viewBox="0 0 1200 675" xmlns="http://www.w3.org/2000/svg">
      <circle class="title__ring" cx="562" cy="338" r="311" fill="none" stroke="var(--brand-orange)" stroke-width="2.5"/>
      <text class="title__kicker" x="562" y="184" text-anchor="middle">DSGVO</text>
      <text class="title__main" x="562" y="275" text-anchor="middle">Netzwerk-</text>
      <text class="title__main" x="562" y="369" text-anchor="middle">workshop</text>
      <line class="title__rule" x1="353" y1="420" x2="770" y2="420" stroke="var(--text-white)" stroke-width="2.5"/>
      <text x="562" y="484" text-anchor="middle"><tspan class="title__focus-label">Schwerpunkt</tspan><tspan class="title__focus-dash"> -</tspan></text>
      <text class="title__focus-topic" x="562" y="547" text-anchor="middle">Firewall &amp; Switche</text>
    </svg>

    <div class="brand-name">Veradis Consulting</div>
  </main>
</body>
</html>
```